all natural handmade soap company looking for unique stand out packaging design for bar soaps

we are looking for a unique and stand out on the shelf package design for our hand made soaps for grocery stores. we have a package soap box (picture included) but we are looking for a TOP-NOTCH, CUSTOM, STAND OUT DESIGN FOR THEM. I am supplying our current packaging design, but we want something more unique and STAND OUT. PICTURES i AM INCLUDING ARE: 1: OUR CURRENT PACKAGE DESIGN
2: OUR LIQUID SOAP LABELS (WHICH WE LOVE) AND WOULD LIKE THE BAR SOAPS TO BE SIMILAR
3: WILL BE IN A WHITE BOX WITH A LARGE CUT OUT IN FRONT (SEE SAMPLE BOX BROWN KRAFT).

Target Market(s)

VARIOUS CUSTOMERS. We sell to sunlit pantry grocers and various grocery stores

Industry/Entity Type

It Company

Requirements
Must have
• cool, unique look that will stand out from a store shelf
• full color acceptable
• our logo on the round part of the package (front)
• please leave a space for bar codes (usually on bottom of box)
• there is a cut out (front) that is there for people to see, feel and smell the soap
• be creative think outside the box open to fresh new designs
Nice to have
• metallic crescent moon (our logo)
Should not have
• organic cannot appear on the front

```html
<!DOCTYPE html>
<html lang="en">
<head>
<meta charset="utf-8">
<title>Lunavera – Bar Soap Packaging</title>
<link rel="stylesheet" href="https://fonts.googleapis.com/css2?family=Cinzel:wght@400;500&family=Great+Vibes&family=Quicksand:wght@300;400&family=Open+Sans:wght@400;600&display=swap">
<style>
  :root {
    --stage: #a8a298;
    --stage-light: #c9c6c1;
    --box-white: #ffffff;
    --ink: #2b2b2b;
    --sage: #b7bd9a;
    --lemon-band: #f5c000;
    --citrus-band: #f56b4f;
    --lemon-soap-a: #7b7a5c;
    --lemon-soap-b: #8f8c6c;
    --citrus-soap-a: #d3a877;
    --citrus-soap-b: #e6c79c;
    --lemon-art-a: #d9e36a;
    --lemon-art-b: #7fb33a;
    --citrus-art-a: #f7a35c;
    --citrus-art-b: #f26b5b;
  }
  * { margin: 0; padding: 0; box-sizing: border-box; }
  html, body { width: 1200px; height: 968px; overflow: hidden; }
  body {
    background: radial-gradient(ellipse at 50% 35%, var(--stage-light), var(--stage) 70%);
    position: relative; font-family: "Open Sans", sans-serif; color: var(--ink);
  }

  .brand-header {
    position: absolute; left: 0; top: 132px; width: 1048px; text-align: center;
    font-family: "Cinzel", serif; font-size: 38px; letter-spacing: 2px; color: #fff;
  }

  .box-front {
    position: absolute; top: 336px; width: 312px; height: 444px;
    background: var(--box-white); box-shadow: 0 8px 14px rgba(0,0,0,.25);
  }
  .box-front--lemon { left: 104px; }
  .box-front--citrus { left: 494px; }
  .box-front svg.front-art { position: absolute; left: 0; top: 0; }

  .front-brand {
    position: absolute; top: 52px; left: 0; width: 100%; text-align: center;
    font-family: "Cinzel", serif; font-size: 21px; line-height: 28px; letter-spacing: 1px; color: var(--ink);
  }
  .front-brand .brand-dot {
    display: inline-block; width: 12px; height: 12px; border-radius: 50%;
    background: var(--sage); margin-right: 6px; vertical-align: 1px;
  }
  .craft-line {
    position: absolute; top: 358px; width: 100%; text-align: center;
    font-family: "Great Vibes", cursive; font-size: 23px; line-height: 30px;
    word-spacing: 6px; color: var(--ink);
  }
  .soap-band {
    position: absolute; top: 392px; left: 0; width: 100%; height: 25px;
    text-align: center; color: #fff; font-family: "Quicksand", sans-serif;
    font-weight: 300; font-size: 25px; line-height: 24px; word-spacing: 4px;
  }
  .box-front--lemon .soap-band { background: var(--lemon-band); }
  .box-front--citrus .soap-band { background: var(--citrus-band); }
  .net-weight {
    position: absolute; top: 425px; width: 100%; text-align: center; font-size: 8px;
  }

  .box-back {
    position: absolute; left: 860px; top: 300px; width: 300px; height: 480px;
    background: var(--box-white); box-shadow: 0 8px 14px rgba(0,0,0,.25);
    padding: 40px 30px;
  }
  .back-brand { font-family: "Cinzel", serif; font-size: 20px; text-align: center; margin-bottom: 26px; }
  .back-brand .brand-dot {
    display: inline-block; width: 11px; height: 11px; border-radius: 50%;
    background: var(--sage); margin-right: 6px; vertical-align: 1px;
  }
  .ingredients-title { font-family: "Cinzel", serif; font-size: 13px; margin-bottom: 6px; }
  .ingredients-list { font-size: 12px; line-height: 17px; font-weight: 600; margin-bottom: 26px; }
  .origin-band {
    position: absolute; left: 0; bottom: 70px; width: 100%; height: 20px;
    background: var(--citrus-band); color: #fff; font-size: 10px; line-height: 20px; padding-left: 30px;
  }
</style>
</head>
<body>

<div class="brand-header">LUNAVERA</div>

<!-- Lemon front -->
<div class="box-front box-front--lemon">
  <svg class="front-art" width="312" height="444" viewBox="0 0 312 444">
    <defs>
      <linearGradient id="lemonSoap" x1="0" y1="0" x2="1" y2="1">
        <stop offset="0" stop-color="var(--lemon-soap-a)"/>
        <stop offset="1" stop-color="var(--lemon-soap-b)"/>
      </linearGradient>
      <radialGradient id="lemonArt">
        <stop offset="0" stop-color="var(--lemon-art-a)"/>
        <stop offset="1" stop-color="var(--lemon-art-b)"/>
      </radialGradient>
      <path id="lemonArc" d="M 78 140 A 84 84 0 0 0 242 140"/>
      <path id="lemonBadgeTop" d="M 247 120 A 21 21 0 0 1 289 120"/>
      <path id="lemonBadgeBottom" d="M 245 120 A 23 23 0 0 0 291 120"/>
    </defs>
    <rect x="6" y="156" width="298" height="196" fill="url(#lemonSoap)" role="img" aria-label="Lemon soap bar seen through the window"/>
    <circle cx="160" cy="128" r="104" fill="var(--box-white)"/>
    <circle cx="160" cy="140" r="36" fill="url(#lemonArt)" role="img" aria-label="Sliced lemons and limes with mint leaves"/>
    <text font-family="Cinzel, serif" font-size="19" fill="var(--ink)" letter-spacing="1">
      <textPath href="#lemonArc" startOffset="50%" text-anchor="middle">LEMON</textPath>
    </text>
    <circle cx="268" cy="120" r="27" fill="none" stroke="var(--ink)" stroke-width="1"/>
    <text font-family="Cinzel, serif" font-size="6" fill="var(--ink)">
      <textPath href="#lemonBadgeTop" startOffset="50%" text-anchor="middle">NO SULFATES</textPath>
    </text>
    <text font-family="Cinzel, serif" font-size="6" fill="var(--ink)">
      <textPath href="#lemonBadgeBottom" startOffset="50%" text-anchor="middle" dominant-baseline="hanging">NO PARABENS</textPath>
    </text>
    <path d="M261 120 l5 7 l10 -15" fill="none" stroke="var(--ink)" stroke-width="2.5" stroke-linecap="round"/>
  </svg>
  <div class="front-brand"><span class="brand-dot"></span>LUNAVERA</div>
  <div class="craft-line">Handcrafted Artisan</div>
  <div class="soap-band">natural soap</div>
  <div class="net-weight">4.5 oz (127.57 grams)</div>
</div>

<!-- Bergamot & Grapefruit front -->
<div class="box-front box-front--citrus">
  <svg class="front-art" width="312" height="444" viewBox="0 0 312 444">
    <defs>
      <linearGradient id="citrusSoap" x1="0" y1="0" x2="1" y2="1">
        <stop offset="0" stop-color="var(--citrus-soap-a)"/>
        <stop offset="1" stop-color="var(--citrus-soap-b)"/>
      </linearGradient>
      <radialGradient id="citrusArt">
        <stop offset="0" stop-color="var(--citrus-art-a)"/>
        <stop offset="1" stop-color="var(--citrus-art-b)"/>
      </radialGradient>
      <path id="citrusArc" d="M 70 128 A 92 92 0 0 0 250 128"/>
      <path id="citrusBadgeTop" d="M 247 120 A 21 21 0 0 1 289 120"/>
      <path id="citrusBadgeBottom" d="M 245 120 A 23 23 0 0 0 291 120"/>
    </defs>
    <rect x="6" y="156" width="298" height="196" fill="url(#citrusSoap)" role="img" aria-label="Bergamot and grapefruit soap bar seen through the window"/>
    <circle cx="160" cy="128" r="104" fill="var(--box-white)"/>
    <circle cx="160" cy="138" r="34" fill="url(#citrusArt)" role="img" aria-label="Grapefruit, bergamot and orange with leaves"/>
    <text font-family="Cinzel, serif" font-size="15" fill="var(--ink)" letter-spacing=".5">
      <textPath href="#citrusArc" startOffset="50%" text-anchor="middle">BERGAMOT &amp; GRAPEFRUIT</textPath>
    </text>
    <circle cx="268" cy="120" r="27" fill="none" stroke="var(--ink)" stroke-width="1"/>
    <text font-family="Cinzel, serif" font-size="6" fill="var(--ink)">
      <textPath href="#citrusBadgeTop" startOffset="50%" text-anchor="middle">NO SULFATES</textPath>
    </text>
    <text font-family="Cinzel, serif" font-size="6" fill="var(--ink)">
      <textPath href="#citrusBadgeBottom" startOffset="50%" text-anchor="middle" dominant-baseline="hanging">NO PARABENS</textPath>
    </text>
    <path d="M261 120 l5 7 l10 -15" fill="none" stroke="var(--ink)" stroke-width="2.5" stroke-linecap="round"/>
  </svg>
  <div class="front-brand"><span class="brand-dot"></span>LUNAVERA</div>
  <div class="craft-line">Handcrafted Artisan</div>
  <div class="soap-band">natural soap</div>
  <div class="net-weight">4.5 oz (127.57 grams)</div>
</div>

<!-- Back panel -->
<div class="box-back">
  <div class="back-brand"><span class="brand-dot"></span>LUNAVERA</div>
  <div class="ingredients-title">100% Vegan Ingredients</div>
  <p class="ingredients-list">Saponified olive oil, coconut oil, shea butter, castor oil, lemon essential oil, lemon peel, poppy seed, sea salt, aloe leaf juice, vitamin E.</p>
  <div class="ingredients-title">100% Vegan Ingredients</div>
  <p class="ingredients-list">Saponified olive oil, coconut oil, bergamot and grapefruit oils.</p>
  <div class="origin-band">MADE IN CA - USA</div>
</div>

</body>
</html>
```